Business Card Design Project

Lindel Cove Pediatric Dentistry is a, kids dental office, located in prestigious Fairhaven Millbrook DC, just blocks from the copper lodge. We are fee for service office that has great patients who value their dental care.

Contact Information for Business Card

I have attached our logo files in black and white, we would like our logo on our cards as well.

```html
<!DOCTYPE html>
<html lang="en">
<head>
<meta charset="utf-8">
<title>Lindel Cove Pediatric Dentistry – Business Cards</title>
<link href="https://fonts.googleapis.com/css2?family=Cinzel:wght@500&family=Lato:wght@400&display=swap" rel="stylesheet">
<style>
  :root {
    --backdrop: #e4e4e6;
    --card-light: #fbfbfa;
    --card-dark: #0b0b0c;
    --ink: #1c1c1c;
    --ink-soft: #3a3a3a;
    --rule: #8a8a8a;
    --paper-text: #f1f1f1;
  }
  * { box-sizing: border-box; margin: 0; padding: 0; }
  html, body { width: 1200px; height: 590px; overflow: hidden; }
  body {
    background: var(--backdrop);
    font-family: "Lato", Arial, sans-serif;
    position: relative;
  }
  .card {
    position: absolute;
    top: 152px;
    width: 500px;
    height: 286px;
    box-shadow: 0 6px 18px rgba(0,0,0,0.12);
  }
  .card--front { left: 60px; background: var(--card-light); color: var(--ink); }
  .card--back { left: 640px; background: var(--card-dark); color: var(--paper-text); }

  .brand {
    font-family: "Cinzel", Georgia, serif;
    font-weight: 500;
    text-align: center;
    line-height: 1.15;
  }
  .card--front .brand {
    position: absolute;
    left: 28px;
    top: 112px;
    width: 180px;
    font-size: 17px;
    color: var(--ink);
  }
  .card--back .brand {
    position: absolute;
    left: 0; right: 0;
    top: 108px;
    font-size: 30px;
    letter-spacing: 1px;
    color: var(--paper-text);
  }

  .details {
    position: absolute;
    left: 238px;
    top: 48px;
  }
  .details__group {
    border-left: 1px solid var(--rule);
    padding-left: 12px;
    margin-bottom: 12px;
  }
  .person__name {
    font-family: "Cinzel", Georgia, serif;
    font-weight: 500;
    font-size: 20px;
    letter-spacing: 0.5px;
    line-height: 1.1;
  }
  .person__role, .address, .contact__item {
    font-size: 12px;
    color: var(--ink-soft);
    line-height: 1.55;
  }
  .contact__item { display: flex; align-items: center; gap: 8px; }
  .contact__icon { width: 11px; height: 11px; fill: var(--ink); flex: none; }
</style>
</head>
<body>
  <section class="card card--front">
    <div class="brand">Lindel Cove<br>Pediatric Dentistry</div>

    <div class="details">
      <div class="details__group person">
        <div class="person__name">Martin Hale</div>
        <div class="person__role">Founder &amp; CEO</div>
      </div>
      <div class="details__group address">
        Suite LC2204, 14-16, Ashgrove Road<br>
        Fairhaven Millbrook DC
      </div>
      <div class="details__group contact">
        <div class="contact__item">
          <svg class="contact__icon" viewBox="0 0 24 24" aria-hidden="true"><path d="M6.6 10.8a15 15 0 0 0 6.6 6.6l2.2-2.2a1 1 0 0 1 1-.25 11.4 11.4 0 0 0 3.6.57 1 1 0 0 1 1 1V20a1 1 0 0 1-1 1A17 17 0 0 1 3 4a1 1 0 0 1 1-1h3.5a1 1 0 0 1 1 1 11.4 11.4 0 0 0 .57 3.6 1 1 0 0 1-.25 1z"/></svg>
          <span>202 555 0147</span>
        </div>
        <div class="contact__item">
          <svg class="contact__icon" viewBox="0 0 24 24" aria-hidden="true"><path d="M2 5h20l-10 8z"/><path d="M2 7.5l10 8 10-8V19H2z"/></svg>
          <span>info@lindelcove.com</span>
        </div>
        <div class="contact__item">
          <svg class="contact__icon" viewBox="0 0 24 24" aria-hidden="true"><circle cx="12" cy="12" r="10"/><path d="M2 12h20M12 2c3 3 3 17 0 20M12 2c-3 3-3 17 0 20" stroke="#fbfbfa" stroke-width="1.5" fill="none"/></svg>
          <span>www.lindelcove.com</span>
        </div>
      </div>
    </div>
  </section>

  <section class="card card--back">
    <div class="brand">Lindel Cove<br>Pediatric Dentistry</div>
  </section>
</body>
</html>
```